Business Card Design Project

Oil & gas fabrication and Paint company. Need double sided with color. want original look. see attached but don't make similar!

Think Steel!

Business

```html
<!DOCTYPE html>
<html lang="en">
<head>
<meta charset="utf-8">
<title>Kestrel Fabrication &amp; Paint – Business Card</title>
<link href="https://fonts.googleapis.com/css2?family=Bree+Serif&family=Open+Sans:wght@400;600&display=swap" rel="stylesheet">
<style>
  :root{
    --backdrop:#e4e1dc;
    --card-white:#ffffff;
    --navy:#1f2a78;
    --ink:#2a2a2a;
    --grey-band:#b9bbbd;
    --orange-light:#ffc24a;
    --orange-deep:#f4a00e;
  }
  html,body{margin:0;padding:0;overflow:hidden;}
  body{width:1200px;height:439px;background:var(--backdrop);position:relative;
       font-family:"Open Sans",Arial,sans-serif;color:var(--ink);}
  .card{position:absolute;top:62px;width:540px;height:315px;overflow:hidden;
        box-shadow:0 6px 18px rgba(0,0,0,.25);}
  .card--front{left:36px;background:var(--card-white);}
  .card--back{left:624px;background:radial-gradient(ellipse at 50% 35%,var(--orange-light),var(--orange-deep) 75%);}
  .card__bands{position:absolute;left:0;bottom:0;width:540px;height:80px;}
  .brand{display:flex;align-items:center;justify-content:center;gap:10px;
         font-family:"Bree Serif",Georgia,serif;color:var(--navy);}
  .brand__dot{width:14px;height:14px;border-radius:50%;background:var(--navy);}
  .card--front .brand{position:absolute;top:46px;left:0;right:0;font-size:34px;}
  .person{position:absolute;left:40px;top:140px;width:220px;text-align:right;}
  .person__name{font-family:"Bree Serif",Georgia,serif;color:var(--navy);font-size:24px;margin:0 0 12px;}
  .line{display:flex;align-items:center;justify-content:flex-end;gap:8px;font-size:14px;margin:4px 0;}
  .line svg{width:14px;height:14px;flex:none;fill:var(--ink);}
  .company-info{position:absolute;left:290px;top:138px;padding-left:16px;
                border-left:1px solid #cfd0d2;font-size:14px;}
  .company-info .line{justify-content:flex-start;}
  .company-info address{font-style:normal;margin-bottom:10px;line-height:1.35;}
  .card--back .brand{position:absolute;top:110px;left:0;right:0;font-size:52px;}
  .card--back .web{position:absolute;top:232px;left:0;right:0;text-align:center;
                   font-size:20px;font-weight:600;color:#2a2a2a;}
</style>
</head>
<body>

<section class="card card--front" aria-label="Card front">
  <div class="brand"><span class="brand__dot"></span>Kestrel Fabrication &amp; Paint</div>

  <div class="person">
    <h1 class="person__name">Dale Morrow</h1>
    <div class="line"><svg viewBox="0 0 14 14"><rect x="4" y="1" width="6" height="12" rx="1"/></svg>713-555-0148</div>
    <div class="line"><svg viewBox="0 0 14 14"><path d="M1 4h12v8H1z M1 4l6 4 6-4" fill="none" stroke="#2a2a2a" stroke-width="1.4"/></svg>dale@kestrelequip.net</div>
    <div class="line">1-888-5-STEEL UP</div>
  </div>

  <div class="company-info">
    <address>4820 N. Industrial Pkwy<br>Pinecrest, TX 77390</address>
    <div class="line"><svg viewBox="0 0 14 14"><path d="M3 1l3 3-2 2a8 8 0 0 0 4 4l2-2 3 3-2 2C5 13 1 9 1 3z"/></svg>281-555-0172</div>
    <div class="line"><svg viewBox="0 0 14 14"><rect x="1" y="5" width="12" height="7" rx="1"/><rect x="4" y="1" width="6" height="4"/></svg>1-888-555-0134</div>
    <div class="line"><svg viewBox="0 0 14 14"><circle cx="7" cy="7" r="6" fill="none" stroke="#2a2a2a" stroke-width="1.3"/><path d="M1 7h12M7 1c-3 3-3 9 0 12M7 1c3 3 3 9 0 12" fill="none" stroke="#2a2a2a" stroke-width="1"/></svg>www.kestrelequip.net</div>
  </div>

  <svg class="card__bands" viewBox="0 0 540 80" aria-hidden="true">
    <polygon points="0,58 250,58 225,80 0,80" fill="var(--grey-band)"/>
    <polygon points="255,40 540,14 540,30 248,58" fill="var(--navy)"/>
    <polygon points="248,58 540,30 540,80 225,80" fill="var(--card-white)"/>
  </svg>
</section>

<section class="card card--back" aria-label="Card back">
  <div class="brand"><span class="brand__dot"></span>Kestrel</div>
  <div class="web">www.kestrelequip.net</div>
</section>

</body>
</html>
```